Healthcare Technology Presentation Folder + Proposal Front Page + Letter Head

We require someone to come up with stationery design theme the following

- Presentation Folders - Template supplied
- Proposal Front Page - A4
- Letter Head - A4

I've provided our company logo, and also the presentation folder template to use.
The Letter head template and Proposal front page design is to be provided in Microsoft Word. Presentation Folder to be provided on the template we have supplied or so long as the dimensions match.

We are looking for a new fresh look, professional design with our target audience being healthcare professionals. Prefer the colour scheme of our logo and traditional black

The presentation folder is to look professional, have our website address tarvelhub.com.au and no other information. Some nice accompanying graphics.

The Letter Head / Proposal Front page must have the following information
- Our logo
- Suite 38, 219 Kendrow Street
Port Melbourne, Victoria, 3184
- Phone: 03 9417 3865
- Fax: 03 9582 4716
- Web: tarvelhub.com.au

The winning design must contain all three designs with a consistent look and feel

Target Market(s)

Healthcare Professional

Font styles to use
Sans Serif

Requirements
Must have
• Our company colours
Should not have
• Healthcare Symbols

```html
<!DOCTYPE html>
<html lang="en">
<head>
<meta charset="utf-8">
<title>Tarvelhub Letterhead</title>
<link rel="stylesheet" href="https://fonts.googleapis.com/css2?family=Barlow:wght@400;500;600&display=swap">
<style>
  :root {
    --backdrop: #e4e4e4;
    --paper: #ffffff;
    --navy: #3b4f75;
    --rule: #5a6f96;
    --footer-ink: #4d6391;
    --body-ink: #1c1c1c;
    --facet-blue: #a9bfe0;
    --facet-pale: #e6edf8;
  }
  * { box-sizing: border-box; margin: 0; padding: 0; }
  html, body {
    width: 1191px;
    height: 1200px;
    overflow: hidden;
    background: var(--backdrop);
  }
  .letterhead {
    position: absolute;
    left: 185px;
    top: 20px;
    width: 821px;
    height: 1160px;
    background: var(--paper);
    font-family: "Barlow", sans-serif;
    overflow: hidden;
  }
  .header-facets {
    position: absolute;
    left: 0; top: 0;
    width: 100%;
    height: 290px;
    background:
      linear-gradient(160deg, var(--facet-blue) 0%, rgba(169,191,224,0.45) 22%, rgba(230,237,248,0.6) 45%, rgba(255,255,255,0) 100%),
      linear-gradient(200deg, rgba(169,191,224,0.7) 0%, rgba(230,237,248,0.3) 30%, rgba(255,255,255,0) 60%);
  }
  .brand {
    position: absolute;
    left: 60px;
    top: 66px;
    display: flex;
    align-items: center;
    gap: 14px;
  }
  .brand-mark {
    width: 40px;
    height: 40px;
    border-radius: 50%;
    background: var(--navy);
  }
  .brand-name {
    font-size: 50px;
    font-weight: 500;
    color: var(--navy);
    letter-spacing: -0.5px;
    line-height: 1;
  }
  .header-rule {
    position: absolute;
    left: 398px;
    right: 0;
    top: 120px;
    height: 2px;
    background: var(--rule);
  }
  .header-web {
    position: absolute;
    right: 38px;
    top: 99px;
    font-size: 13px;
    color: var(--navy);
  }
  .letter-body {
    position: absolute;
    left: 84px;
    top: 270px;
    width: 644px;
    font-size: 15.3px;
    line-height: 16px;
    color: var(--body-ink);
    hyphens: auto;
  }
  .letter-body p + p { margin-top: 16px; }
  .footer {
    position: absolute;
    left: 204px;
    width: 402px;
    top: 1100px;
    border-top: 1.5px solid var(--rule);
    padding-top: 5px;
    text-align: center;
    font-size: 11px;
    line-height: 14px;
    font-weight: 500;
    color: var(--footer-ink);
  }
</style>
</head>
<body>
  <main class="letterhead">
    <div class="header-facets" role="img" aria-label="Soft pale blue faceted geometric band across the top of the page"></div>

    <header>
      <div class="brand">
        <span class="brand-mark"></span>
        <span class="brand-name">Tarvelhub</span>
      </div>
      <div class="header-rule"></div>
      <div class="header-web">tarvelhub.com.au</div>
    </header>

    <section class="letter-body">
      <p>Lorem ipsum dolor sit amet, consectetur adipiscing elit. Pellentesque id interdum nisl, nec pellentesque ligula. Nunc at orci id erat egestas lobortis at ut ipsum. Etiam iaculis quam consectetur, pretium erat ac, venenatis massa. Cras quis enim mi. Nulla ac magna purus. Pellentesque ut leo lacinia, molestie nisi non, porttitor erat. Praesent metus dolor, malesuada id laoreet vitae, luctus elementum justo. Nunc id consectetur metus. Vestibulum eget sapien eget leo suscipit molestie et pharetra dolor. Cras id dictum turpis. Duis eros lorem, ullamcorper elementum tempus id, varius ut diam. Proin id condimentum lorem. Proin eu turpis tincidunt, laoreet enim nec, suscipit massa. Nunc id elit non purus bibendum molestie.</p>
      <p>Curabitur nisi tellus, porta et neque eu, vehicula posuere erat. Etiam mattis, nunc non luctus suscipit, nisl lectus sodales eros, ut venenatis diam massa et ipsum. Nam scelerisque, sapien sed tristique posuere, nibh mi molestie elit, vitae imperdiet erat augue sit amet nulla. Duis eget viverra urna, quis fringilla nibh. Nulla consequat egestas vestibulum. Nullam mollis, ipsum et faucibus bibendum, tellus risus faucibus sapien, vitae tristique odio sapien sit amet elit. Pellentesque non leo lacinia, rutrum enim a, pellentesque elit.</p>
      <p>Suspendisse nec tempor sapien, sed tincidunt purus. Suspendisse potenti. Donec elit lorem, consequat vitae tortor vel, tempus rhoncus ligula. Cras non neque id quam ullamcorper tempus a in magna. Fusce adipiscing molestie ligula, vitae bibendum felis sollicitudin eu. Suspendisse in dui vel odio varius blandit vitae eget ante. Donec egestas odio ut est scelerisque ullamcorper. Vestibulum sit amet leo luctus, laoreet metus a, mattis arcu. Vivamus porta lectus nulla, quis sagittis neque faucibus et.</p>
    </section>

    <footer class="footer">
      <div class="footer-address">Suite 38, 219 Kendrow Street, Port Melbourne, Victoria, 3184</div>
      <div class="footer-contact">Phone: 03 9417 3865, Fax: 03 9582 4716</div>
    </footer>
  </main>
</body>
</html>
```